Mastering the Art of Challenging Conversations

I need a professional powerpoint presentation to use when teaching corporate workshops about how to handle hard conversations. I want it to be colorful, but not cartoonish. The images I attached are from quellin snap photos - I like the colors and the look of the image with the people and the conversation and thought "bubbles" above their heads. I also like the image of the two conversation bubbles with heads inside the bubbles. The slides will not have a lot of text on them so the design will be prominent. I'm also open to the idea of stock photos showing people engaged in both frustrating and successful conversations.

Target Market(s)

Corporate Managers

Industry/Entity Type

Corporate Talent Development

Font styles to use
Sans Serif

Colors
0094D4
00A9DD
6FCCEA
C7EBF8
E9F6FB
F0912C
F2A743
F7CA91
FBE8D2
FDF5EE
6B429C
8869AF
B7A5CE
E3DAEB
F3F0F8

Requirements
Must have
• An uncluttered look - professional, but not stuffy. Colorful but not cartoonish,
Nice to have
• The presentation is all about how to have conversations. So conversation and thought bubbles should be used in the design but not overdone.
Should not have
• cartoons, clip art, patterns (only solid colors for fill in and backgrounds)

```html
<!DOCTYPE html>
<html lang="en">
<head>
<meta charset="utf-8">
<title>Mastering the Art of Challenging Conversations – Workshop Deck</title>
<link rel="stylesheet" href="https://fonts.googleapis.com/css2?family=Montserrat:wght@500;700;800&family=Oswald:wght@500;700&family=Roboto:wght@300;400;500;700;900&display=swap">
<style>
:root{
  --blue:#0094d4;
  --blue-bright:#00a9dd;
  --blue-sky:#6fccea;
  --blue-pale:#c7ebf8;
  --blue-mist:#e9f6fb;
  --orange:#f0912c;
  --orange-soft:#f2a743;
  --peach:#f7ca91;
  --purple:#6b429c;
  --purple-mid:#8869af;
  --lilac:#b7a5ce;
  --lilac-pale:#e3daeb;
  --ink:#2c2f33;
  --grey-text:#555a60;
  --board:#9ea2a6;
  --white:#ffffff;
}
*{box-sizing:border-box;margin:0;padding:0}
html,body{width:903px;height:1200px;overflow:hidden}
body{background:var(--board);font-family:"Roboto",Arial,sans-serif;color:var(--ink);position:relative}
.slide{position:absolute;width:279px;height:157px;overflow:hidden;background:var(--white);box-shadow:0 2px 5px rgba(0,0,0,.35)}
.slide.blue{background:var(--blue)}
.slide.purple{background:var(--purple)}
.abs{position:absolute}
.photo{position:absolute}
.pg{position:absolute;right:9px;bottom:7px;font:700 4.4px "Montserrat",sans-serif;color:var(--blue)}
.pg.light{color:var(--white)}
.body{font-size:3.3px;line-height:1.45;color:var(--grey-text)}
.body p{margin-bottom:3px}
.body.white{color:#fff}
.just{text-align:justify}
.h-thin{font-family:"Roboto",sans-serif;font-weight:400}
.c-blue{color:var(--blue)} .c-orange{color:var(--orange)} .c-white{color:var(--white)} .c-purple{color:var(--purple)}
.web{font:500 6px "Roboto",sans-serif;letter-spacing:1.6px;color:var(--ink)}
.web b{color:var(--orange);font-weight:500}
.soc{display:flex;gap:3px}
.soc i{display:block;width:9px;height:9px;background:var(--blue);border-radius:2px}
.soc.round i{background:none;border:1px solid var(--white);border-radius:50%;width:10px;height:10px}
.framebox{position:absolute;border:1px solid var(--white);display:flex;flex-direction:column;align-items:center;justify-content:center;font:700 22px/1.08 "Oswald",sans-serif;color:var(--white);letter-spacing:.3px}
.framebox span{color:var(--orange-soft)}
.ticklist{list-style:none;font:300 6.4px/1 "Roboto",sans-serif;color:var(--ink)}
.ticklist li{display:flex;align-items:center;gap:4px;margin-bottom:5.2px}
.sq{width:2.4px;height:2.4px;background:var(--orange);display:inline-block}
.bullets{list-style:none}
.bullets li{display:flex;gap:3px;margin-bottom:4px;font-size:3.2px;line-height:1.4}
.tri{width:0;height:0;border-left:4px solid var(--orange);border-top:2.4px solid transparent;border-bottom:2.4px solid transparent;flex:none;margin-top:1px}
.tri.faint{opacity:.55}
.tri.white{border-left-color:var(--white)}
.iconcircle{position:absolute;width:22px;height:22px;border-radius:50%;background:var(--orange);border:2px solid var(--white);box-shadow:0 0 0 1.2px var(--orange)}
.item-title{font:700 6px "Roboto",sans-serif;color:var(--orange)}
.member{position:absolute;top:78px;width:50px;text-align:center}
.member .av{width:24px;height:24px;margin:0 auto;border-radius:50%;border:1.5px solid var(--orange);background:var(--peach)}
.member h4{font:700 4.6px "Montserrat",sans-serif;color:var(--white);margin-top:4px}
.member p{font-size:2.5px;line-height:1.4;color:#fff;margin-top:1px}
</style>
</head>
<body>

<!-- Row 1 -->
<section class="slide" style="left:23px;top:22px">
  <div class="photo" role="img" aria-label="Two colleagues in a tense but respectful conversation at an office desk" style="left:112px;top:0;width:167px;height:157px;background:var(--blue-pale)"></div>
  <div class="abs h-thin c-blue" style="left:11px;top:46px;font-size:6.4px">MASTERING THE ART OF</div>
  <div class="abs c-orange" style="left:10px;top:55px;font:900 13.5px 'Roboto',sans-serif">CHALLENGING</div>
  <div class="abs c-blue" style="left:11px;top:72px;font:700 9.6px 'Roboto',sans-serif">CONVERSATIONS</div>
  <div class="abs" style="left:11px;top:88px;width:44px;height:1.6px;background:var(--orange)"></div>
  <div class="abs web" style="left:11px;top:93px;font-size:5.4px;letter-spacing:1.3px">www.<b>talkwellhub</b>.com</div>
  <div class="abs soc" style="left:11px;top:105px"><i></i><i></i><i></i><i></i></div>
</section>

<section class="slide blue" style="left:312px;top:22px">
  <div class="abs c-white h-thin" style="left:0;right:0;top:38px;text-align:center;font-size:9.5px">MASTERING THE ART OF</div>
  <div class="abs c-orange" style="left:0;right:0;top:50px;text-align:center;font:900 25px 'Roboto',sans-serif">CHALLENGING</div>
  <div class="abs c-white" style="left:0;right:0;top:80px;text-align:center;font:700 14px 'Roboto',sans-serif">CONVERSATIONS</div>
  <div class="abs" style="left:117px;top:102px;width:45px;height:1.6px;background:var(--orange)"></div>
  <div class="abs web" style="left:0;right:0;top:108px;text-align:center;color:#fff">www.<b>talkwellhub</b>.com</div>
  <div class="abs soc round" style="left:126px;top:122px"><i></i><i></i></div>
</section>

<section class="slide" style="left:600px;top:22px">
  <div class="photo" role="img" aria-label="Manager standing by a window, ready to talk" style="left:0;top:0;width:108px;height:157px;background:var(--lilac)"></div>
  <div class="abs c-blue" style="left:62px;top:71px;background:#fff;border-radius:11px;padding:1px 7px;font:700 15px 'Montserrat',sans-serif">Contents</div>
  <div class="abs" style="left:140px;top:24px;width:128px">
    <div style="margin-bottom:11px"><div class="item-title"><span class="c-blue">1.</span>&nbsp; Why talks go wrong</div><div class="body" style="margin-left:10px;font-size:3px">Listen first, then speak with care so every voice feels heard and respected.</div></div>
    <div style="margin-bottom:11px"><div class="item-title"><span class="c-blue">2.</span>&nbsp; Prepare with purpose</div><div class="body" style="margin-left:10px;font-size:3px">Listen first, then speak with care so every voice feels heard and respected.</div></div>
    <div style="margin-bottom:11px"><div class="item-title"><span class="c-blue">3.</span>&nbsp; Listen to understand</div><div class="body" style="margin-left:10px;font-size:3px">Listen first, then speak with care so every voice feels heard and respected.</div></div>
    <div><div class="item-title"><span class="c-blue">4.</span>&nbsp; Agree on next steps</div><div class="body" style="margin-left:10px;font-size:3px">Listen first, then speak with care so every voice feels heard and respected.</div></div>
  </div>
  <div class="pg">02</div>
</section>

<!-- Row 2 -->
<section class="slide blue" style="left:23px;top:190px">
  <div class="framebox" style="left:89px;top:34px;width:100px;height:89px">WHY<span>THIS</span>MATTERS</div>
</section>

<section class="slide" style="left:312px;top:190px">
  <div class="abs" style="left:10px;top:11px;width:139px;height:132px;background:var(--blue)"></div>
  <div class="abs c-white" style="left:20px;top:22px;font:500 11px/1.25 'Montserrat',sans-serif">ABOUT THIS<br><b style="font-weight:800">WORKSHOP</b></div>
  <div class="abs body white just" style="left:20px;top:57px;width:112px">
    <p>Hard talks go better when both sides share a clear goal. Start with facts, name the feeling, and ask open questions. Keep your tone calm and your words simple so the other person can stay engaged.</p>
    <p>Hard talks go better when both sides share a clear goal. Start with facts, name the feeling, and ask open questions. Keep your tone calm and your words simple so the other person can stay engaged.</p>
  </div>
  <div class="iconcircle" style="left:138px;top:20px"></div>
  <div class="iconcircle" style="left:138px;top:66px"></div>
  <div class="iconcircle" style="left:138px;top:110px"></div>
  <svg class="abs" style="left:143px;top:25px" width="12" height="12" viewBox="0 0 12 12" fill="none" stroke="#fff" stroke-width="1"><path d="M1.5 2h9v6H5l-2.5 2V8h-1z"/></svg>
  <svg class="abs" style="left:143px;top:71px" width="12" height="12" viewBox="0 0 12 12" fill="none" stroke="#fff" stroke-width="1"><circle cx="6" cy="5" r="3.5"/><path d="M4.5 10.5h3"/></svg>
  <svg class="abs" style="left:143px;top:115px" width="12" height="12" viewBox="0 0 12 12" fill="#fff" stroke="#fff" stroke-width=".9"><path d="M2 9 5 5 7 7 10 3" fill="none"/><circle cx="2" cy="9" r="1.1"/><circle cx="5" cy="5" r="1.1"/><circle cx="7" cy="7" r="1.1"/><circle cx="10" cy="3" r="1.1"/></svg>
  <div class="abs" style="left:167px;top:16px;width:100px">
    <div class="item-title">Set the stage</div>
    <div class="body" style="font-size:3px;margin-bottom:23px">Listen first, then speak with care so every voice feels heard and respected.</div>
    <div class="item-title">Hear the story</div>
    <div class="body" style="font-size:3px;margin-bottom:20px">Listen first, then speak with care so every voice feels heard and respected.</div>
    <div class="item-title">Find the path</div>
    <div class="body" style="font-size:3px">Listen first, then speak with care so every voice feels heard and respected.</div>
  </div>
  <div class="pg">05</div>
</section>

<section class="slide" style="left:600px;top:190px">
  <div class="photo" role="img" aria-label="Smiling woman pointing at an empty speech bubble" style="inset:0;background:var(--lilac-pale)"></div>
  <div class="abs c-orange h-thin" style="left:9px;top:8px;font-size:9px">WHEN WORDS</div>
  <div class="abs c-blue" style="left:9px;top:18px;font:800 8.6px 'Montserrat',sans-serif">GET DIFFICULT</div>
  <div class="pg">06</div>
</section>

<!-- Row 3 -->
<section class="slide" style="left:23px;top:357px">
  <div class="abs" style="left:0;top:21px;width:149px;height:118px;background:var(--blue)"></div>
  <div class="abs c-white" style="left:13px;top:24px;font:400 10px/1.15 'Montserrat',sans-serif">WHY TALKS<br><b style="font-weight:700">GO SIDEWAYS</b></div>
  <ul class="abs" style="left:14px;top:51px;width:130px;list-style:disc;color:#fff;font-size:3.3px;line-height:1.4">
    <li style="margin-bottom:4px"><b>Assumptions :</b> Pause before you reply, check what you heard, and agree on one next step together.</li>
    <li style="margin-bottom:4px"><b>Emotion :</b> Pause before you reply, check what you heard, and agree on one next step together.</li>
    <li style="margin-bottom:4px"><b>Timing :</b> Pause before you reply, check what you heard, and agree on one next step together.</li>
    <li style="margin-bottom:4px"><b>Tone :</b> Pause before you reply, check what you heard, and agree on one next step together.</li>
    <li><b>Silence :</b> Pause before you reply, check what you heard, and agree on one next step together.</li>
  </ul>
  <div class="abs" style="left:157px;top:20px;font:500 8.3px/1.45 'Montserrat',sans-serif">
    <div class="c-blue">WHY IS IT HARD?</div>
    <div class="c-blue">IT'S THE FEAR WE</div>
    <div class="c-orange" style="font-weight:800">BRING INTO THE ROOM.</div>
  </div>
  <ul class="abs ticklist" style="left:157px;top:66px">
    <li><span class="sq"></span>Stay curious, not defensive</li>
    <li><span class="sq"></span>Name the issue, not the person</li>
    <li><span class="sq"></span>Stay curious, not defensive</li>
    <li><span class="sq"></span>Name the issue, not the person</li>
    <li><span class="sq"></span>Stay curious, not defensive</li>
    <li><span class="sq"></span>Name the issue, not the person</li>
  </ul>
  <div class="pg">07</div>
</section>

<section class="slide" style="left:312px;top:357px">
  <div class="photo" role="img" aria-label="Two colleagues holding red and yellow speech bubbles against an orange wall" style="inset:0;background:var(--peach)"></div>
  <div class="abs c-orange h-thin" style="left:152px;top:10px;font-size:11.5px">SPEAK UP</div>
  <div class="abs c-blue" style="left:152px;top:24px;font:800 11.5px 'Montserrat',sans-serif">SAY IT CLEARLY</div>
  <div class="pg">08</div>
</section>

<section class="slide purple" style="left:600px;top:357px">
  <div class="framebox" style="left:89px;top:37px;width:100px;height:88px">THE<span>CORE</span>SKILLS</div>
</section>

<!-- Row 4 -->
<section class="slide" style="left:23px;top:523px">
  <div class="photo" role="img" aria-label="Three colleagues holding a large empty speech bubble" style="inset:0;background:var(--lilac)"></div>
  <div class="pg light">10</div>
</section>

<section class="slide" style="left:312px;top:523px">
  <div class="abs c-blue" style="left:11px;top:17px;font:800 10px 'Montserrat',sans-serif">WORKSHOP</div>
  <div class="abs c-orange" style="left:11px;top:27px;font:800 14.5px 'Montserrat',sans-serif">OUTCOMES</div>
  <div class="abs body" style="left:11px;top:48px;width:113px">
    <p>Hard talks go better when both sides share a clear goal. Start with facts, name the feeling, and ask open questions. Keep your tone calm and your words simple so the other person can stay engaged.</p>
    <p>Pause before you reply, check what you heard, and agree on one next step together.</p>
  </div>
  <svg class="abs" style="left:135px;top:13px" width="135" height="72" viewBox="0 0 135 72" font-family="Roboto,sans-serif">
    <g stroke="#d5d8dc" stroke-width=".4">
      <line x1="14" y1="6" x2="132" y2="6"/><line x1="14" y1="15.5" x2="132" y2="15.5"/><line x1="14" y1="25" x2="132" y2="25"/><line x1="14" y1="34.5" x2="132" y2="34.5"/><line x1="14" y1="44" x2="132" y2="44"/><line x1="14" y1="53.5" x2="132" y2="53.5"/>
      <line x1="14" y1="6" x2="14" y2="63"/><line x1="132" y1="6" x2="132" y2="63"/>
    </g>
    <line x1="14" y1="63" x2="132" y2="63" stroke="#666" stroke-width=".5"/>
    <g font-size="4" fill="#444" text-anchor="end">
      <text x="11" y="7.5">60</text><text x="11" y="17">50</text><text x="11" y="26.5">40</text><text x="11" y="36">30</text><text x="11" y="45.5">20</text><text x="11" y="55">10</text><text x="11" y="64.5">0</text>
    </g>
    <g fill="#0094d4"><rect x="26" y="25" width="3.5" height="38"/><rect x="51" y="29.8" width="3.5" height="33.2"/><rect x="78" y="7.9" width="3.5" height="55.1"/><rect x="106" y="34.5" width="3.5" height="28.5"/></g>
    <g fill="#f0912c"><rect x="30" y="15.5" width="3.5" height="47.5"/><rect x="47" y="53.5" width="3.5" height="9.5"/><rect x="82" y="50.6" width="3.5" height="12.4"/><rect x="102" y="13.6" width="3.5" height="49.4"/></g>
    <g font-size="4" fill="#444" text-anchor="middle"><text x="30" y="70">JAN</text><text x="51" y="70">FEB</text><text x="82" y="70">MAR</text><text x="106" y="70">APR</text></g>
  </svg>
  <svg class="abs" style="left:10px;top:92px" width="125" height="52" viewBox="0 0 125 52" font-family="Roboto,sans-serif">
    <g stroke="#e1e3e6" stroke-width=".35"><line x1="12" y1="3" x2="122" y2="3"/><line x1="12" y1="10" x2="122" y2="10"/><line x1="12" y1="17" x2="122" y2="17"/><line x1="12" y1="24" x2="122" y2="24"/><line x1="12" y1="31" x2="122" y2="31"/><line x1="12" y1="38" x2="122" y2="38"/></g>
    <line x1="12" y1="45" x2="122" y2="45" stroke="#666" stroke-width=".4"/>
    <line x1="12" y1="3" x2="12" y2="45" stroke="#666" stroke-width=".4"/>
    <g font-size="3.2" fill="#444" text-anchor="end"><text x="9" y="4">60</text><text x="9" y="11">50</text><text x="9" y="18">40</text><text x="9" y="25">30</text><text x="9" y="32">20</text><text x="9" y="39">10</text><text x="9" y="46">0</text></g>
    <polyline points="17,39 29,43 41,24 53,35 65,21 77,31 89,27 101,25 113,16" fill="none" stroke="#0094d4" stroke-width=".6"/>
    <polyline points="17,35 29,38 41,27 53,15 65,22 77,27 89,22 101,17 113,36" fill="none" stroke="#f0912c" stroke-width=".6"/>
    <g fill="#0094d4"><circle cx="17" cy="39" r=".9"/><circle cx="29" cy="43" r=".9"/><circle cx="41" cy="24" r=".9"/><circle cx="53" cy="35" r=".9"/><circle cx="65" cy="21" r=".9"/><circle cx="77" cy="31" r=".9"/><circle cx="89" cy="27" r=".9"/><circle cx="101" cy="25" r=".9"/><circle cx="113" cy="16" r=".9"/></g>
    <g fill="#f0912c"><circle cx="17" cy="35" r=".9"/><circle cx="29" cy="38" r=".9"/><circle cx="41" cy="27" r=".9"/><circle cx="53" cy="15" r=".9"/><circle cx="65" cy="22" r=".9"/><circle cx="77" cy="27" r=".9"/><circle cx="89" cy="22" r=".9"/><circle cx="101" cy="17" r=".9"/><circle cx="113" cy="36" r=".9"/></g>
    <g font-size="2.2" fill="#444" text-anchor="middle"><text x="17" y="49">WEEK 1</text><text x="29" y="49">WEEK 2</text><text x="41" y="49">WEEK 3</text><text x="53" y="49">WEEK 4</text><text x="65" y="49">WEEK 5</text><text x="77" y="49">WEEK 6</text><text x="89" y="49">WEEK 7</text><text x="101" y="49">WEEK 8</text><text x="113" y="49">WEEK 9</text></g>
  </svg>
  <div class="abs" style="left:137px;top:97px;width:135px;display:grid;grid-template-columns:1fr 1fr;row-gap:9px;column-gap:6px">
    <div style="display:flex;gap:3px"><span style="width:4.5px;height:4.5px;border-radius:50%;background:var(--orange);flex:none;margin-top:1px"></span><div><div class="c-orange" style="font-size:5px">Confidence</div><div class="body" style="font-size:2.6px">Short note on the monthly trend line.</div></div></div>
    <div style="display:flex;gap:3px"><span style="width:4.5px;height:4.5px;border-radius:50%;background:var(--blue);flex:none;margin-top:1px"></span><div><div class="c-blue" style="font-size:5px">Clarity</div><div class="body" style="font-size:2.6px">Short note on the monthly trend line.</div></div></div>
    <div style="display:flex;gap:3px"><span style="width:4.5px;height:4.5px;border-radius:50%;background:var(--blue);flex:none;margin-top:1px"></span><div><div class="c-blue" style="font-size:5px">Trust</div><div class="body" style="font-size:2.6px">Short note on the monthly trend line.</div></div></div>
    <div style="display:flex;gap:3px"><span style="width:4.5px;height:4.5px;border-radius:50%;background:var(--orange);flex:none;margin-top:1px"></span><div><div class="c-orange" style="font-size:5px">Follow-up</div><div class="body" style="font-size:2.6px">Short note on the monthly trend line.</div></div></div>
  </div>
  <div class="pg">11</div>
</section>

<section class="slide" style="left:600px;top:523px">
  <div class="photo" role="img" aria-label="Three colleagues holding red, yellow and blue speech bubbles against a teal wall" style="inset:0;background:var(--blue-sky)"></div>
  <div class="pg light">12</div>
</section>

<!-- Row 5 -->
<section class="slide" style="left:23px;top:689px">
  <div class="abs" style="left:13px;top:12px;width:144px;height:2px;background:var(--blue)"></div>
  <div class="abs" style="left:155px;top:12px;width:2px;height:39px;background:var(--blue)"></div>
  <div class="abs" style="left:13px;top:105px;width:2px;height:40px;background:var(--blue)"></div>
  <div class="abs" style="left:13px;top:143px;width:54px;height:2px;background:var(--blue)"></div>
  <div class="photo" role="img" aria-label="Excited man bursting through yellow paper holding a speech bubble" style="left:22px;top:21px;width:125px;height:115px;background:var(--orange-soft)"></div>
  <div class="abs c-orange h-thin" style="left:169px;top:15px;font-size:7px">PUTTING SKILLS INTO</div>
  <div class="abs c-blue" style="left:168px;top:22px;font:800 14px 'Montserrat',sans-serif">PRACTICE</div>
  <div class="abs body just" style="left:169px;top:40px;width:96px">
    <p>Hard talks go better when both sides share a clear goal. Start with facts, name the feeling, and ask open questions. Keep your tone calm and your words simple so the other person can stay engaged.</p>
    <p>Hard talks go better when both sides share a clear goal. Start with facts, name the feeling, and ask open questions. Keep your tone calm and your words simple so the other person can stay engaged.</p>
  </div>
  <ul class="abs bullets body" style="left:169px;top:107px;width:96px">
    <li><span class="tri"></span><span>Pause before you reply, check what you heard, and agree on one next step together.</span></li>
    <li style="margin-top:6px"><span class="tri faint"></span><span>Pause before you reply, check what you heard, and agree on one next step together.</span></li>
  </ul>
  <div class="pg">13</div>
</section>

<section class="slide" style="left:312px;top:689px">
  <div class="photo" role="img" aria-label="Diverse group holding colourful speech bubbles above their heads outdoors" style="inset:0;background:var(--blue-pale)"></div>
  <div class="abs" style="left:14px;top:100px;width:91px;height:40px;background:var(--blue)"></div>
  <div class="abs c-white" style="left:18px;top:107px;font:500 11px/1.15 'Montserrat',sans-serif">STARTING<br><b style="font-weight:800">THE TALK</b></div>
  <div class="abs" style="left:105px;top:99px;width:160px;height:41px;background:var(--orange)"></div>
  <div class="abs" style="left:110px;top:101px;width:152px;font-size:2.8px;line-height:1.35;color:#fff">
    <p style="margin-bottom:2px">Hard talks go better when both sides share a clear goal. Start with facts, name the feeling, and ask open questions. Keep your tone calm and your words simple so the other person can stay engaged.</p>
    <p>Hard talks go better when both sides share a clear goal. Start with facts, name the feeling, and ask open questions. Keep your tone calm and your words simple so the other person can stay engaged.</p>
  </div>
  <div class="pg">14</div>
</section>

<section class="slide" style="left:600px;top:689px">
  <div class="abs" style="left:14px;top:10px;width:91px;height:40px;background:var(--blue)"></div>
  <div class="abs c-white" style="left:18px;top:18px;font:500 7px/1.25 'Montserrat',sans-serif">OUR MODEL OF<br><b style="font-weight:800;font-size:13px">APPROACH</b></div>
  <div class="abs" style="left:106px;top:10px;width:159px;height:40px;background:var(--orange)"></div>
  <div class="abs" style="left:111px;top:12px;width:151px;font-size:2.8px;line-height:1.35;color:#fff">
    <p style="margin-bottom:2px">Hard talks go better when both sides share a clear goal. Start with facts, name the feeling, and ask open questions. Keep your tone calm and your words simple so the other person can stay engaged.</p>
    <p>Hard talks go better when both sides share a clear goal. Start with facts, name the feeling, and ask open questions. Keep your tone calm and your words simple so the other person can stay engaged.</p>
  </div>
  <div class="photo" role="img" aria-label="Row of eight people standing under colourful speech bubbles" style="left:12px;top:56px;width:256px;height:84px;background:var(--lilac-pale)"></div>
  <div class="pg">15</div>
</section>

<!-- Row 6 -->
<section class="slide" style="left:23px;top:855px">
  <div class="abs" style="left:19px;top:12px;width:72px;height:2px;background:var(--blue)"></div>
  <div class="abs" style="left:158px;top:24px;width:2px;height:112px;background:var(--blue)"></div>
  <div class="abs" style="left:131px;top:134px;width:29px;height:2px;background:var(--blue)"></div>
  <div class="photo" role="img" aria-label="Man surrounded by coloured speech bubbles held by many hands" style="left:0;top:17px;width:158px;height:117px;background:var(--blue-mist)"></div>
  <div class="abs c-orange h-thin" style="left:174px;top:20px;font-size:9px">ACTIVE</div>
  <div class="abs c-blue" style="left:174px;top:31px;font:800 8.6px 'Montserrat',sans-serif">LISTENING</div>
  <div class="abs body just" style="left:174px;top:43px;width:93px">
    <p>Hard talks go better when both sides share a clear goal. Start with facts, name the feeling, and ask open questions. Keep your tone calm and your words simple so the other person can stay engaged.</p>
    <p>Hard talks go better when both sides share a clear goal. Start with facts, name the feeling, and ask open questions. Keep your tone calm and your words simple so the other person can stay engaged.</p>
  </div>
  <ul class="abs bullets body" style="left:174px;top:107px;width:93px">
    <li><span class="tri"></span><span>Pause before you reply, check what you heard, and agree on one next step together.</span></li>
    <li style="margin-top:6px"><span class="tri faint"></span><span>Pause before you reply, check what you heard, and agree on one next step together.</span></li>
  </ul>
  <div class="pg">16</div>
</section>

<section class="slide" style="left:312px;top:855px">
  <div class="abs" style="left:8px;top:9px;width:136px;height:137px;background:var(--purple)"></div>
  <div class="abs c-white" style="left:17px;top:16px;font:500 9.3px/1.15 'Montserrat',sans-serif">FRUSTRATING<br><b style="font-weight:800">CONVERSATIONS</b></div>
  <div class="abs body white just" style="left:17px;top:39px;width:120px">
    <p>Hard talks go better when both sides share a clear goal. Start with facts, name the feeling, and ask open questions. Keep your tone calm and your words simple so the other person can stay engaged.</p>
    <p>Hard talks go better when both sides share a clear goal. Start with facts, name the feeling, and ask open questions. Keep your tone calm and your words simple so the other person can stay engaged.</p>
  </div>
  <ul class="abs bullets" style="left:17px;top:107px;width:120px;color:#fff">
    <li><span class="tri white"></span><span>Pause before you reply, check what you heard, and agree on one next step together.</span></li>
    <li style="margin-top:6px"><span class="tri white faint"></span><span>Pause before you reply, check what you heard, and agree on one next step together.</span></li>
  </ul>
  <div class="abs c-orange" style="left:151px;top:16px;font:500 9.3px/1.15 'Montserrat',sans-serif">SUCCESSFUL<br><b class="c-blue" style="font-weight:800">CONVERSATIONS</b></div>
  <div class="abs body just" style="left:151px;top:39px;width:117px">
    <p>Hard talks go better when both sides share a clear goal. Start with facts, name the feeling, and ask open questions. Keep your tone calm and your words simple so the other person can stay engaged.</p>
    <p>Hard talks go better when both sides share a clear goal. Start with facts, name the feeling, and ask open questions. Keep your tone calm and your words simple so the other person can stay engaged.</p>
  </div>
  <ul class="abs bullets body" style="left:151px;top:107px;width:117px">
    <li><span class="tri"></span><span>Pause before you reply, check what you heard, and agree on one next step together.</span></li>
    <li style="margin-top:6px"><span class="tri faint"></span><span>Pause before you reply, check what you heard, and agree on one next step together.</span></li>
  </ul>
  <div class="pg">17</div>
</section>

<section class="slide" style="left:600px;top:855px">
  <div class="abs" style="left:10px;top:70px;width:2px;height:67px;background:var(--blue)"></div>
  <div class="abs" style="left:10px;top:135px;width:54px;height:2px;background:var(--blue)"></div>
  <div class="photo" role="img" aria-label="Thoughtful man holding a speech bubble against a dark wall" style="left:18px;top:14px;width:111px;height:123px;background:var(--purple-mid)"></div>
  <div class="abs c-orange h-thin" style="left:139px;top:14px;font-size:10.5px">BENEFITS FOR EACH</div>
  <div class="abs c-blue" style="left:139px;top:26px;font:800 10px 'Montserrat',sans-serif">MANAGER AND TEAM</div>
  <div class="abs body just" style="left:139px;top:41px;width:130px">
    <p>Hard talks go better when both sides share a clear goal. Start with facts, name the feeling, and ask open questions. Keep your tone calm and your words simple so the other person can stay engaged.</p>
    <p>Hard talks go better when both sides share a clear goal. Start with facts, name the feeling, and ask open questions. Keep your tone calm and your words simple so the other person can stay engaged.</p>
    <p>Hard talks go better when both sides share a clear goal. Start with facts, name the feeling, and ask open questions. Keep your tone calm and your words simple so the other person can stay engaged.</p>
    <p>Hard talks go better when both sides share a clear goal. Start with facts, name the feeling, and ask open questions. Keep your tone calm and your words simple so the other person can stay engaged.</p>
  </div>
  <div class="pg">18</div>
</section>

<!-- Row 7 -->
<section class="slide" style="left:23px;top:1021px">
  <div class="photo" role="img" aria-label="Two colleagues talking outside an office building" style="left:131px;top:0;width:148px;height:157px;background:var(--lilac)"></div>
  <div class="abs" style="left:12px;top:20px;font:500 8.4px/1.45 'Montserrat',sans-serif">
    <div class="c-blue">WHAT HELPS MOST?</div>
    <div class="c-blue">SIMPLE HABITS THAT</div>
    <div class="c-orange" style="font-weight:800">KEEP TALKS ON TRACK.</div>
  </div>
  <ul class="abs ticklist" style="left:12px;top:65px;font-size:6.2px">
    <li><svg width="5" height="5" viewBox="0 0 5 5"><path d="M.5 2.6 2 4 4.6 .9" fill="none" stroke="#2c2f33" stroke-width=".6"/></svg>&nbsp;Ask before you assume</li>
    <li><svg width="5" height="5" viewBox="0 0 5 5"><path d="M.5 2.6 2 4 4.6 .9" fill="none" stroke="#2c2f33" stroke-width=".6"/></svg>&nbsp;Repeat back what you heard</li>
    <li><svg width="5" height="5" viewBox="0 0 5 5"><path d="M.5 2.6 2 4 4.6 .9" fill="none" stroke="#2c2f33" stroke-width=".6"/></svg>&nbsp;Ask before you assume</li>
    <li><svg width="5" height="5" viewBox="0 0 5 5"><path d="M.5 2.6 2 4 4.6 .9" fill="none" stroke="#2c2f33" stroke-width=".6"/></svg>&nbsp;Repeat back what you heard</li>
    <li><svg width="5" height="5" viewBox="0 0 5 5"><path d="M.5 2.6 2 4 4.6 .9" fill="none" stroke="#2c2f33" stroke-width=".6"/></svg>&nbsp;Ask before you assume</li>
    <li><svg width="5" height="5" viewBox="0 0 5 5"><path d="M.5 2.6 2 4 4.6 .9" fill="none" stroke="#2c2f33" stroke-width=".6"/></svg>&nbsp;Repeat back what you heard</li>
  </ul>
  <div class="pg light">19</div>
</section>

<section class="slide" style="left:312px;top:1021px">
  <div class="abs" style="left:0;right:0;top:16px;text-align:center;font:500 9px 'Montserrat',sans-serif"><span class="c-orange">FACILITATORS</span> <b class="c-blue" style="font-weight:800">AND</b> <span class="c-orange">ADVISORS</span></div>
  <div class="abs body" style="left:16px;top:29px;width:247px;text-align:center;font-size:3px">
    <p>Hard talks go better when both sides share a clear goal. Start with facts, name the feeling, and ask open questions. Keep your tone calm and your words simple so the other person can stay engaged.</p>
    <p>Hard talks go better when both sides share a clear goal. Start with facts, name the feeling, and ask open questions. Keep your tone calm and your words simple so the other person can stay engaged.</p>
  </div>
  <div class="abs" style="left:0;top:71px;width:279px;height:64px;background:var(--blue)"></div>
  <div class="member" style="left:14px"><div class="av" role="img" aria-label="Facilitator portrait"></div><h4>OWEN MARSH</h4><p>Listen first, then speak with care so every voice feels heard and respected.</p></div>
  <div class="member" style="left:82px"><div class="av" role="img" aria-label="Facilitator portrait"></div><h4>IDA FENWICK</h4><p>Listen first, then speak with care so every voice feels heard and respected.</p></div>
  <div class="member" style="left:147px"><div class="av" role="img" aria-label="Advisor portrait"></div><h4>OWEN MARSH</h4><p>Listen first, then speak with care so every voice feels heard and respected.</p></div>
  <div class="member" style="left:214px"><div class="av" role="img" aria-label="Advisor portrait"></div><h4>IDA FENWICK</h4><p>Listen first, then speak with care so every voice feels heard and respected.</p></div>
  <div class="pg">20</div>
</section>

<section class="slide blue" style="left:600px;top:1021px">
  <div class="abs c-white" style="left:0;right:0;top:43px;text-align:center;font:700 28px 'Oswald',sans-serif;letter-spacing:.5px">THANK YOU</div>
  <div class="abs c-white h-thin" style="left:55px;top:81px;font-size:10px">CONTACT <b class="c-orange" style="font-weight:700">US</b></div>
  <div class="abs c-white" style="left:127px;top:78px;font-size:6px;line-height:1.5">
    <div style="display:flex;align-items:center;gap:3px"><svg width="5" height="5" viewBox="0 0 10 10"><circle cx="5" cy="5" r="5" fill="#f0912c"/><path d="M3 2.5 4.2 2.3 4.8 3.8 4 4.4a4 4 0 0 0 1.6 1.6l.6-.8 1.5.6-.2 1.2A4.5 4.5 0 0 1 3 2.5z" fill="#fff"/></svg>555-204-118</div>
    <div style="display:flex;align-items:center;gap:3px"><svg width="5" height="5" viewBox="0 0 10 10"><circle cx="5" cy="5" r="5" fill="#f0912c"/><rect x="2.5" y="3.2" width="5" height="3.6" fill="#fff"/></svg>hello@talkwellhub.com</div>
    <div style="display:flex;align-items:center;gap:3px"><svg width="5" height="5" viewBox="0 0 10 10"><circle cx="5" cy="5" r="5" fill="#f0912c"/><path d="M5 2a2 2 0 0 1 2 2c0 1.5-2 4-2 4S3 5.5 3 4a2 2 0 0 1 2-2z" fill="#fff"/></svg>12 Harbor Lane, Ashford, 40417</div>
  </div>
  <div class="abs web" style="left:0;right:0;top:114px;text-align:center;color:#fff">www.<b>talkwellhub</b>.com</div>
  <div class="abs soc round" style="left:126px;top:126px"><i></i><i></i></div>
</section>

</body>
</html>
```